Small Business coaching and services company

Need a powerpoint template design for a company that provides Human Resources services as well sales and business coaching.

```html
<!DOCTYPE html>
<html lang="en">
<head>
<meta charset="utf-8">
<title>Business Presentation Template</title>
<link href="https://fonts.googleapis.com/css2?family=Poppins:ital,wght@0,400;0,500;0,600;0,700;1,400;1,500&display=swap" rel="stylesheet">
<style>
  :root {
    --amber: #F7A823;
    --amber-deep: #E9A12A;
    --ink: #1F1409;
    --body: #2b2b2b;
    --page: #ffffff;
    --mist: #ececec;
    --photo-a: #d9dcdf;
    --photo-b: #8a8f96;
  }
  * { margin: 0; padding: 0; box-sizing: border-box; }
  html, body { width: 1200px; height: 970px; overflow: hidden; background: var(--page); }
  body { position: relative; font-family: "Poppins", sans-serif; color: var(--ink); }

  .frame { position: absolute; }
  .frame--hero { left: 280px; top: 36px; width: 640px; height: 359px; }
  .frame--grid { width: 360px; height: 202px; }
  .slide {
    position: absolute; left: 0; top: 0; width: 583px; height: 327px;
    background: var(--page); overflow: hidden; transform-origin: 0 0;
    box-shadow: 2px 3px 6px rgba(0,0,0,.25);
  }
  .frame--hero .slide { transform: scale(1.0978); }
  .frame--grid .slide { transform: scale(0.6175); }

  .shapes { position: absolute; inset: 0; width: 583px; height: 327px; }
  .photo { position: absolute; }
  .t { position: absolute; }

  .heading { font-weight: 700; font-size: 20px; letter-spacing: .2px; text-transform: uppercase; }
  .heading-rule { position: absolute; width: 54px; height: 2px; background: var(--amber); }
  .quote { font-style: italic; font-size: 11px; line-height: 15px; color: var(--ink); }
  .quote .mark { color: var(--amber); }
  .body-text { font-size: 7.4px; line-height: 13px; color: var(--body); }
  .item-title { font-size: 10.5px; font-weight: 500; text-transform: uppercase; }
  .item-text { font-size: 7.4px; line-height: 11.5px; color: var(--body); margin-top: 4px; }
  .site { font-size: 11px; color: #fff; letter-spacing: .2px; }

  .icon-box { position: absolute; width: 58px; height: 58px; background: var(--amber); display: flex; align-items: center; justify-content: center; }
  .icon-box svg { width: 34px; height: 34px; }
  .icon-box--sm { width: 50px; height: 50px; }
  .icon-box--sm svg { width: 30px; height: 30px; }

  .cover-title { font-size: 36px; font-weight: 700; line-height: 40px; letter-spacing: .3px; color: var(--ink); }
  .brand { display: flex; align-items: center; gap: 7px; font-size: 17px; font-weight: 600; color: var(--amber); }
  .brand .dot { width: 14px; height: 14px; border-radius: 50%; background: var(--amber); }

  .member-photo { position: absolute; width: 58px; height: 58px; background: linear-gradient(135deg, #e4e4e4, #bcbcbc); display: flex; align-items: center; justify-content: center; text-align: center; font-size: 4px; color: #888; line-height: 5px; }

  .thanks-title { font-size: 36px; font-weight: 700; color: var(--ink); }
  .thanks-text { font-size: 10.5px; line-height: 16px; color: var(--ink); }
  .contact-label { font-size: 10px; font-weight: 500; }
  .contact-row { display: flex; align-items: center; gap: 8px; font-size: 10px; margin-top: 7px; }
  .contact-row svg { width: 11px; height: 11px; }
</style>
</head>
<body>

<!-- Cover slide, shown large -->
<div class="frame frame--hero">
  <section class="slide slide--cover">
    <div class="photo" role="img" aria-label="Photo of a business team talking in a bright office" style="left:280px;top:0;width:303px;height:327px;background:linear-gradient(160deg,var(--photo-a),var(--photo-b));"></div>
    <svg class="shapes" viewBox="0 0 583 327">
      <polygon points="305,0 345,0 430,160 400,180" fill="var(--amber)" opacity=".7"/>
      <polygon points="0,30 280,30 385,190 330,295 0,295" fill="var(--amber)"/>
      <polygon points="330,305 410,305 410,327 320,327" fill="var(--page)"/>
      <polygon points="418,285 583,285 583,327 395,327" fill="#f4f4f4"/>
      <rect x="0" y="304" width="340" height="3" fill="var(--amber)"/>
    </svg>
    <div class="t cover-title" style="left:42px;top:92px;">BUSINESS<br>PRESENTATION</div>
    <div class="t quote" style="left:42px;top:193px;width:270px;line-height:18px;">“The printing and typesetting industry. Lorem Ipsum has been the industry’s”</div>
    <div class="t brand" style="left:420px;top:294px;"><span class="dot"></span>Northpeak</div>
  </section>
</div>

<!-- Row 1 -->
<div class="frame frame--grid" style="left:36px;top:440px;">
  <section class="slide slide--cover">
    <div class="photo" role="img" aria-label="Photo of a business team talking in a bright office" style="left:280px;top:0;width:303px;height:327px;background:linear-gradient(160deg,var(--photo-a),var(--photo-b));"></div>
    <svg class="shapes" viewBox="0 0 583 327">
      <polygon points="305,0 345,0 430,160 400,180" fill="var(--amber)" opacity=".7"/>
      <polygon points="0,30 280,30 385,190 330,295 0,295" fill="var(--amber)"/>
      <polygon points="330,305 410,305 410,327 320,327" fill="var(--page)"/>
      <polygon points="418,285 583,285 583,327 395,327" fill="#f4f4f4"/>
      <rect x="0" y="304" width="340" height="3" fill="var(--amber)"/>
    </svg>
    <div class="t cover-title" style="left:42px;top:92px;">BUSINESS<br>PRESENTATION</div>
    <div class="t quote" style="left:42px;top:193px;width:270px;line-height:18px;">“The printing and typesetting industry. Lorem Ipsum has been the industry’s”</div>
    <div class="t brand" style="left:420px;top:294px;"><span class="dot"></span>Northpeak</div>
  </section>
</div>

<div class="frame frame--grid" style="left:420px;top:440px;">
  <section class="slide slide--company">
    <div class="photo" role="img" aria-label="Photo of two colleagues working together at a desk" style="left:0;top:0;width:310px;height:327px;background:linear-gradient(140deg,#e9e6e3,#6e6a68);clip-path:polygon(0 0,172px 0,300px 240px,300px 327px,0 327px);"></div>
    <svg class="shapes" viewBox="0 0 583 327">
      <polygon points="176,0 184,0 263,148 257,152" fill="var(--amber)"/>
      <rect x="0" y="304" width="390" height="3" fill="var(--amber)"/>
      <polygon points="390,285 583,285 583,327 370,327" fill="var(--amber)"/>
    </svg>
    <div class="t heading" style="left:327px;top:60px;">Our Company</div>
    <div class="heading-rule" style="left:327px;top:91px;"></div>
    <div class="t quote" style="left:327px;top:103px;width:215px;"><span class="mark">“</span>Lorem Ipsum is simply dummy text of the printing and typesetting<span class="mark">”</span></div>
    <div class="t body-text" style="left:327px;top:140px;width:225px;">Text of the printing and typesetting industry. Lorem Ipsum has been the industry’s standard dummy text ever since the 1500s, when an unknown printer took a galley of type and scrambled it to make a type specimen book. It has survived not only five centuries, but also the leap into electronic typesetting, remaining</div>
    <div class="t site" style="left:408px;top:299px;">www.northpeak.example</div>
  </section>
</div>

<div class="frame frame--grid" style="left:804px;top:440px;">
  <section class="slide slide--why">
    <svg class="shapes" viewBox="0 0 583 327">
      <polygon points="0,0 205,0 190,25 0,25" fill="var(--amber)"/>
      <rect x="0" y="304" width="390" height="3" fill="var(--amber)"/>
      <polygon points="390,285 583,285 583,327 370,327" fill="var(--amber)"/>
    </svg>
    <div class="t heading" style="left:42px;top:66px;">Why Choose Us</div>
    <div class="heading-rule" style="left:42px;top:96px;"></div>
    <div class="t quote" style="left:42px;top:108px;width:505px;line-height:16px;">Lorem Ipsum is simply dummy text of the printing and typesetting industry. Lorem Ipsum has been the industry’s standard dummy text ever since the 1500s, when an unknown printer took a galley of type and scrambled it to make</div>
    <div class="icon-box" style="left:42px;top:181px;">
      <svg viewBox="0 0 34 34" fill="none" stroke="var(--ink)" stroke-width="2.2"><rect x="5" y="4" width="24" height="26"/><circle cx="17" cy="14" r="4.5" fill="var(--ink)"/><path d="M9 27c1-6 4-8 8-8s7 2 8 8z" fill="var(--ink)"/></svg>
    </div>
    <div class="t" style="left:115px;top:186px;width:165px;"><div class="item-title">Lorem Ipsum</div><div class="item-text">Lorem Ipsum is simply dummy text of the printing and typesetting industry. Lorem Ipsum has been the industry’s</div></div>
    <div class="icon-box" style="left:296px;top:181px;">
      <svg viewBox="0 0 34 34" fill="none" stroke="var(--ink)" stroke-width="2.2"><rect x="5" y="4" width="24" height="26"/><rect x="10" y="19" width="3" height="7" fill="var(--ink)"/><rect x="15.5" y="14" width="3" height="12" fill="var(--ink)"/><rect x="21" y="9" width="3" height="17" fill="var(--ink)"/></svg>
    </div>
    <div class="t" style="left:369px;top:186px;width:165px;"><div class="item-title">Lorem Ipsum</div><div class="item-text">Lorem Ipsum is simply dummy text of the printing and typesetting industry. Lorem Ipsum has been the industry’s</div></div>
    <div class="t site" style="left:408px;top:299px;">www.northpeak.example</div>
  </section>
</div>

<!-- Row 2 -->
<div class="frame frame--grid" style="left:36px;top:700px;">
  <section class="slide slide--team">
    <svg class="shapes" viewBox="0 0 583 327">
      <polygon points="0,0 205,0 190,25 0,25" fill="var(--amber)"/>
      <rect x="0" y="304" width="390" height="3" fill="var(--amber)"/>
      <polygon points="390,285 583,285 583,327 370,327" fill="var(--amber)"/>
    </svg>
    <div class="t heading" style="left:42px;top:66px;">Our Team Members</div>
    <div class="heading-rule" style="left:42px;top:96px;"></div>
    <div class="member-photo" role="img" aria-label="Team member photo" style="left:42px;top:119px;">PLACE YOUR<br>IMAGE</div>
    <div class="t" style="left:115px;top:122px;width:165px;"><div class="item-title">Lorem Ipsum</div><div class="item-text">Lorem Ipsum is simply dummy text of the printing and typesetting industry. Lorem Ipsum has been the industry’s</div></div>
    <div class="member-photo" role="img" aria-label="Team member photo" style="left:300px;top:119px;">PLACE YOUR<br>IMAGE</div>
    <div class="t" style="left:373px;top:122px;width:165px;"><div class="item-title">Lorem Ipsum</div><div class="item-text">Lorem Ipsum is simply dummy text of the printing and typesetting industry. Lorem Ipsum has been the industry’s</div></div>
    <div class="member-photo" role="img" aria-label="Team member photo" style="left:42px;top:198px;">PLACE YOUR<br>IMAGE</div>
    <div class="t" style="left:115px;top:201px;width:165px;"><div class="item-title">Lorem Ipsum</div><div class="item-text">Lorem Ipsum is simply dummy text of the printing and typesetting industry. Lorem Ipsum has been the industry’s</div></div>
    <div class="member-photo" role="img" aria-label="Team member photo" style="left:300px;top:198px;">PLACE YOUR<br>IMAGE</div>
    <div class="t" style="left:373px;top:201px;width:165px;"><div class="item-title">Lorem Ipsum</div><div class="item-text">Lorem Ipsum is simply dummy text of the printing and typesetting industry. Lorem Ipsum has been the industry’s</div></div>
    <div class="t site" style="left:408px;top:299px;">www.northpeak.example</div>
  </section>
</div>

<div class="frame frame--grid" style="left:420px;top:700px;">
  <section class="slide slide--services">
    <svg class="shapes" viewBox="0 0 583 327">
      <polygon points="0,0 205,0 190,25 0,25" fill="var(--amber)"/>
      <rect x="0" y="304" width="390" height="3" fill="var(--amber)"/>
      <polygon points="390,285 583,285 583,327 370,327" fill="var(--amber)"/>
    </svg>
    <div class="t heading" style="left:42px;top:40px;">Our Services</div>
    <div class="heading-rule" style="left:42px;top:70px;"></div>
    <div class="icon-box icon-box--sm" style="left:46px;top:86px;">
      <svg viewBox="0 0 30 30" fill="none" stroke="var(--ink)" stroke-width="1.8"><rect x="4" y="9" width="22" height="15" rx="2"/><path d="M11 9V6h8v3M4 15h22"/></svg>
    </div>
    <div class="t" style="left:115px;top:86px;width:170px;"><div class="item-title">Lorem Ipsum</div><div class="item-text">Lorem Ipsum is simply dummy text of the printing and typesetting industry. Lorem Ipsum has been the industry’s</div></div>
    <div class="icon-box icon-box--sm" style="left:46px;top:153px;">
      <svg viewBox="0 0 30 30" fill="none" stroke="var(--ink)" stroke-width="1.8"><rect x="4" y="5" width="22" height="16"/><path d="M15 21v4M10 26h10M9 17v-3M13 17v-6M17 17v-4M21 17v-8"/></svg>
    </div>
    <div class="t" style="left:115px;top:153px;width:170px;"><div class="item-title">Lorem Ipsum</div><div class="item-text">Lorem Ipsum is simply dummy text of the printing and typesetting industry. Lorem Ipsum has been the industry’s</div></div>
    <div class="icon-box icon-box--sm" style="left:46px;top:221px;">
      <svg viewBox="0 0 30 30" fill="none" stroke="var(--ink)" stroke-width="1.8"><circle cx="15" cy="15" r="11"/><ellipse cx="15" cy="15" rx="5" ry="11"/><path d="M4 15h22M6 9h18M6 21h18"/></svg>
    </div>
    <div class="t" style="left:115px;top:221px;width:170px;"><div class="item-title">Lorem Ipsum</div><div class="item-text">Lorem Ipsum is simply dummy text of the printing and typesetting industry. Lorem Ipsum has been the industry’s</div></div>
    <div class="t" style="left:342px;top:108px;width:225px;font-size:11.5px;font-weight:500;line-height:18px;">The printing and typesetting industry. Lorem Ipsum has been the industry’s standard dummy text ever since the 1500s, when an unknown printer took a galley of type and scrambled</div>
    <div class="t site" style="left:408px;top:299px;">www.northpeak.example</div>
  </section>
</div>

<div class="frame frame--grid" style="left:804px;top:700px;">
  <section class="slide slide--thanks">
    <svg class="shapes" viewBox="0 0 583 327">
      <polygon points="0,0 410,0 518,160 442,327 0,327" fill="var(--amber)"/>
      <polygon points="445,0 492,0 560,118 536,158" fill="var(--amber)"/>
      <polygon points="488,327 583,165 583,327" fill="var(--mist)"/>
    </svg>
    <div class="t thanks-title" style="left:84px;top:56px;">THANK YOU</div>
    <div class="t thanks-text" style="left:84px;top:111px;width:330px;">Text of the printing and typesetting industry. Lorem Ipsum has been the industry’s standard dummy text ever since the 1500s, when an unknown printer took</div>
    <div class="t" style="left:84px;top:190px;">
      <div class="contact-label">GET IN TOUCH</div>
      <div class="contact-row" style="margin-top:18px;"><svg viewBox="0 0 12 12"><path d="M1 4c0-2 2-3 5-3s5 1 5 3l-2 1-1-2H4L3 5zM3 6h6l1 5H2z" fill="var(--ink)"/></svg>+000 1234 6789</div>
      <div class="contact-row"><svg viewBox="0 0 12 12"><path d="M6 1a3.5 3.5 0 0 1 3.5 3.5C9.5 7 6 11 6 11S2.5 7 2.5 4.5A3.5 3.5 0 0 1 6 1z" fill="var(--ink)"/><circle cx="6" cy="4.5" r="1.3" fill="var(--amber)"/></svg>Street Name, City Name, Country Name</div>
    </div>
  </section>
</div>

</body>
</html>
```